Fast Growing Personal Injury Law Firm Needs Business Card Design

We need a business card design for a fast growing personal injury law firm in Florida. Our name is Darren Kolvisty, P.A. Our practice is comprised of younger attorneys (in their 30s) that employ more modern techniques/tools than our older competition. We would prefer a look that is a modern play on a classic look. Also, we would like to continue using a color scheme that employs navy blue and kelly green (other shades of green could be fine too) as well as our "E" logo.

Industry/Entity Type

Law Firm

```html
<!DOCTYPE html>
<html lang="en">
<head>
<meta charset="utf-8">
<title>Darren Kolvisty, P.A. — Business Card</title>
<link rel="stylesheet" href="https://fonts.googleapis.com/css2?family=Libre+Baskerville:wght@700&family=Montserrat:wght@400;500;700&display=swap">
<style>
  :root {
    --navy: #1a237e;
    --green: #1e8a3c;
    --paper: #ffffff;
    --ink: #444444;
    --rule: #5c67b8;
    --backdrop: #3f4a48;
  }
  * { box-sizing: border-box; margin: 0; padding: 0; }
  html, body { width: 1200px; height: 900px; overflow: hidden; }
  body {
    background: var(--backdrop);
    font-family: "Montserrat", sans-serif;
    position: relative;
  }
  .card {
    position: absolute;
    left: 250px;
    width: 700px;
    height: 400px;
    background: var(--paper);
    overflow: hidden;
    box-shadow: 0 10px 30px rgba(0,0,0,.35);
  }
  .card--front { top: 25px; }
  .card--back { top: 475px; }

  .firm {
    position: absolute;
    display: flex;
    align-items: center;
    gap: 14px;
  }
  .firm__mark {
    width: 54px; height: 54px;
    background: var(--green);
    flex: none;
  }
  .firm__name {
    font-family: "Libre Baskerville", serif;
    font-weight: 700;
    color: var(--navy);
    font-size: 26px;
    line-height: 1.1;
    letter-spacing: .5px;
  }
  .firm__tagline {
    font-family: "Libre Baskerville", serif;
    font-weight: 700;
    color: var(--green);
    font-size: 18px;
    letter-spacing: 1.5px;
    margin-top: 2px;
  }
  .card--front .firm { left: 40px; top: 40px; }

  .rule {
    position: absolute;
    height: 1px;
    background: var(--rule);
  }
  .card--front .rule { left: 40px; right: 40px; top: 198px; }

  .attorney {
    position: absolute;
    right: 40px;
    top: 140px;
    text-align: right;
  }
  .attorney__name {
    font-weight: 700;
    color: var(--navy);
    font-size: 24px;
    letter-spacing: 3px;
  }
  .attorney__title {
    font-size: 16px;
    color: var(--ink);
    letter-spacing: 2px;
    margin-top: 12px;
  }

  .contact {
    position: absolute;
    left: 40px;
    bottom: 68px;
    list-style: none;
    font-size: 16px;
    color: var(--ink);
    letter-spacing: 1.2px;
    line-height: 1.45;
  }
  .contact li { display: flex; align-items: center; gap: 8px; }
  .contact svg { width: 13px; height: 13px; fill: var(--navy); flex: none; }

  .address {
    position: absolute;
    right: 40px;
    bottom: 68px;
    text-align: right;
    font-style: normal;
    font-size: 16px;
    color: var(--ink);
    line-height: 1.45;
  }
  .address svg { width: 14px; height: 11px; vertical-align: -1px; margin-left: 6px; }

  .band {
    position: absolute;
    left: 0; right: 0; bottom: 0;
    height: 34px;
    background: var(--green);
    border-top: 3px solid var(--paper);
    box-shadow: 0 -2px 0 var(--navy);
  }

  .card--back .firm { left: 60px; top: 230px; }
  .card--back .rule { left: 200px; right: 0; top: 292px; }
  .web {
    position: absolute;
    right: 40px;
    top: 264px;
    font-size: 16px;
    color: var(--navy);
    letter-spacing: 1.5px;
  }
</style>
</head>
<body>

<section class="card card--front" aria-label="Card front">
  <div class="firm">
    <div class="firm__mark"></div>
    <div>
      <div class="firm__name">Darren Kolvisty, P.A.</div>
      <div class="firm__tagline">Personal Injury Attorneys</div>
    </div>
  </div>

  <div class="attorney">
    <div class="attorney__name">Darren Kolvisty</div>
    <div class="attorney__title">Attorney at Law</div>
  </div>
  <div class="rule"></div>

  <ul class="contact">
    <li><svg viewBox="0 0 16 16" aria-hidden="true"><path d="M1 5c0-2 3-3 7-3s7 1 7 3v1h-4V5H5v1H1zM3 8l2-2h6l2 2v6H3z"/></svg>(941) 555-0142</li>
    <li><svg viewBox="0 0 16 16" aria-hidden="true"><path d="M4 1h6v4H4zM2 6h12v7H2zM4 8v3h8V8z"/></svg>(941) 555-0187</li>
    <li><svg viewBox="0 0 16 16" aria-hidden="true"><path d="M8 0a8 8 0 100 16A8 8 0 008 0zm5.9 7h-2.9a12 12 0 00-1-5 6 6 0 013.9 5zM8 2c.8 1 1.4 2.8 1.5 5h-3C6.6 4.8 7.2 3 8 2zM6 2a12 12 0 00-1 5H2.1A6 6 0 016 2zM2.1 9H5a12 12 0 001 5 6 6 0 01-3.9-5zM8 14c-.8-1-1.4-2.8-1.5-5h3c-.1 2.2-.7 4-1.5 5zm2 0a12 12 0 001-5h2.9a6 6 0 01-3.9 5z"/></svg>kolvistylaw.com</li>
  </ul>

  <address class="address">
    2150 Harbor Point Drive, Suite 300<br>
    Bayview Springs, Florida 34210<br>
    darren@kolvistylaw.com<svg viewBox="0 0 14 11" aria-hidden="true"><rect x=".5" y=".5" width="13" height="10" fill="none" stroke="#1a237e"/><path d="M.5.5L7 6l6.5-5.5" fill="none" stroke="#1a237e"/></svg>
  </address>

  <div class="band"></div>
</section>

<section class="card card--back" aria-label="Card back">
  <div class="firm">
    <div class="firm__mark"></div>
    <div>
      <div class="firm__name">Darren Kolvisty, P.A.</div>
      <div class="firm__tagline">Personal Injury Attorneys</div>
    </div>
  </div>
  <div class="web">kolvistylaw.com</div>
  <div class="rule"></div>
</section>

</body>
</html>
```